amber meridian consulting needs a business card

i need a business card with a logo that will also be used on the website. The company name is "Amber Meridian Consulting"
The business is an advisory and training organisation that specialises in finding a companys 'natural sequence' to success but we will also provide mentoring and counselling to individuals that want to unlock their potential. The process is unique and not full of the normal corporate bullshit so the card should be 'different' and innovative in use of texture, colour, layout etc...I have no guiding principles for you but if you were the head of a new company lloking to make a great first impression what would your card look like? It should have enough of the corporate that the stiffs dont get scared but should be cool enough that the cool kids get it :-)

Target Market(s)

Companies and people looking to grow their staff capabilities. Specialising in IT but can transcend that to other lines of business.

Industry/Entity Type

It Company

Contact Information for Business Card

usuall placeholder stuff Name, Number etc

Requirements
Must have
• cool and innovative logo and use of space
Nice to have
• Background image, subtle use of the caffeine molecule
• A rollable business card similar to the attached image. Would be nice if either side of the card could be half of a DNA helix and by rolling 2 sides together they could connect at one or more points....Perhaps the strands between have a message?
Should not have
• boring usual business card look and feel

```html
<!DOCTYPE html>
<html lang="en">
<head>
<meta charset="utf-8">
<title>Amber Meridian Consulting – Business Card</title>
<link rel="stylesheet" href="https://fonts.googleapis.com/css2?family=Ubuntu:wght@500&family=Open+Sans:wght@400&display=swap">
<style>
  :root {
    --page: #e9ebed;
    --brand-blue: #1aa8d8;
    --brand-blue-light: #19c2ea;
    --brand-blue-deep: #0a8fc4;
    --card-white: #f7f7f7;
    --ink: #3a3a3a;
  }
  html, body {
    margin: 0;
    width: 1200px;
    height: 1023px;
    overflow: hidden;
    background: var(--page);
  }
  .canvas {
    position: relative;
    width: 1200px;
    height: 1023px;
  }
  .card {
    position: absolute;
    left: 250px;
    width: 700px;
    height: 400px;
    border-radius: 22px;
    overflow: hidden;
    box-shadow: 0 10px 28px rgba(0,0,0,0.18);
  }
  .card-front { top: 70px; }
  .card-back  { top: 553px; }
  .card svg { display: block; }
  .company-name {
    font-family: "Ubuntu", sans-serif;
    font-weight: 500;
  }
  .contact {
    font-family: "Open Sans", sans-serif;
    font-weight: 400;
  }
</style>
</head>
<body>
<main class="canvas">

  <section class="card card-front" aria-label="Business card front">
    <svg width="700" height="400" viewBox="0 0 700 400">
      <defs>
        <linearGradient id="frontBlue" x1="0" y1="0" x2="1" y2="1">
          <stop offset="0" stop-color="#22b6e2"/>
          <stop offset="1" stop-color="#0d96c9"/>
        </linearGradient>
      </defs>
      <rect class="band" width="700" height="400" fill="url(#frontBlue)"/>
      <path class="white-panel" d="M26,0 L430,0 C575,70 610,250 548,400 L26,400 Z" fill="var(--card-white)"/>
      <path class="swoosh" d="M470,4 C600,60 650,220 600,396" fill="none" stroke="#ffffff" stroke-width="7" stroke-linecap="round"/>

      <circle class="name-mark" cx="66" cy="70" r="15" fill="none" stroke="var(--brand-blue)" stroke-width="4"/>
      <text class="company-name" x="92" y="82" font-size="33" fill="var(--brand-blue)">Amber Meridian Consulting</text>

      <text class="company-name" x="150" y="236" font-size="31" fill="var(--brand-blue)">Your Name</text>
      <text class="contact" x="152" y="258" font-size="14" fill="var(--ink)">Title</text>

      <g class="contact-line phone" transform="translate(152,300)">
        <path d="M2,-10 q-3,6 3,12 q6,5 9,2 l-2,-3 q-2,1 -4,-1 q-3,-3 -1,-5 l-2,-3 z" fill="var(--brand-blue)"/>
        <text class="contact" x="20" y="0" font-size="15" fill="var(--ink)">01-555-0142</text>
      </g>
      <g class="contact-line email" transform="translate(152,328)">
        <rect x="0" y="-11" width="13" height="10" fill="none" stroke="var(--brand-blue)" stroke-width="1.5"/>
        <path d="M0,-11 L6.5,-5 L13,-11" fill="none" stroke="var(--brand-blue)" stroke-width="1.5"/>
        <text class="contact" x="20" y="0" font-size="15" fill="var(--ink)">hello@ambermeridian.co.uk</text>
      </g>

      <g class="contact-line web" transform="translate(372,300)">
        <circle cx="6" cy="-5" r="6" fill="none" stroke="var(--brand-blue)" stroke-width="1.5"/>
        <path d="M0,-5 H12 M6,-11 V1" stroke="var(--brand-blue)" stroke-width="1.2"/>
        <text class="contact" x="18" y="0" font-size="15" fill="var(--ink)">www.ambermeridian.co.uk</text>
      </g>
      <g class="contact-line address" transform="translate(372,328)">
        <path d="M6,2 C1,-5 0,-7 0,-9 a6,6 0 0 1 12,0 c0,2 -1,4 -6,11 z" fill="var(--brand-blue)"/>
        <circle cx="6" cy="-9" r="2" fill="#fff"/>
        <text class="contact" x="18" y="0" font-size="15" fill="var(--ink)">Your address</text>
      </g>
    </svg>
  </section>

  <section class="card card-back" aria-label="Business card back">
    <svg width="700" height="400" viewBox="0 0 700 400">
      <defs>
        <radialGradient id="backBlue" cx="0.55" cy="0.45" r="0.8">
          <stop offset="0" stop-color="var(--brand-blue-light)"/>
          <stop offset="1" stop-color="var(--brand-blue-deep)"/>
        </radialGradient>
      </defs>
      <rect width="700" height="400" fill="url(#backBlue)"/>
      <circle class="name-mark" cx="350" cy="150" r="52" fill="none" stroke="#ffffff" stroke-width="8"/>
      <text class="company-name" x="350" y="272" font-size="40" fill="#ffffff" text-anchor="middle">Amber Meridian Consulting</text>
    </svg>
  </section>

</main>
</body>
</html>
```